BRIMLOW Pizza and Wraps

We need a website for a new restaurant called BRIMLOW "PIZZA AND WRAPS".
I have attached fonts, background images, logo, images, content etc.
can provide you with what you need to get the website design done fast and easy

I have uploaded more images of the venue and some menu items. let me know if there is anything I need to provide to make your mission clear and easy

Reason: i would like a little time to provide more feedback to designers

Industry/Entity Type

Restaurant

Coding

Coded - Design and coding required

Number of Pages Required

5+ page

Colors

Designer to choose colors to be used in the design.

Requirements
Must have
• PAGES:
• Our Story
• Menu
• Reservations
• Catering & Delivery
• Contact

```html
<!DOCTYPE html>
<html lang="en">
<head>
<meta charset="utf-8">
<title>BRIMLOW Pizza and Wraps – Home Page</title>
<link rel="stylesheet" href="https://fonts.googleapis.com/css2?family=Josefin+Sans:wght@300;400;600;700&display=swap">
<style>
:root{
  --board:#f3f3f3;
  --ink:#111111;
  --brand-red:#e41e26;
  --white:#ffffff;
  --gold:#b8862c;
  --panel-w:562px;
  --panel-h:308px;
  --band-h:38px;
}
*{box-sizing:border-box;margin:0;padding:0}
html,body{width:1200px;height:1200px;overflow:hidden;background:var(--board)}
body{position:relative;font-family:"Josefin Sans",sans-serif;color:var(--ink)}
.board-title{position:absolute;top:32px;left:0;width:1200px;text-align:center;font-weight:700;font-size:38px;letter-spacing:2px}

.screen{position:absolute;width:var(--panel-w);height:var(--panel-h);overflow:hidden;background:#222}
.screen--1{left:26px;top:108px}
.screen--2{left:613px;top:108px}
.screen--3{left:26px;top:479px}
.screen--4{left:613px;top:479px}
.screen--5{left:26px;top:847px}

.caption{position:absolute;width:562px;text-align:center;font-size:16px;letter-spacing:1px;font-weight:300}
.caption b{font-weight:700;font-variant:small-caps;font-size:19px}
.caption--1{left:26px;top:424px}
.caption--2{left:613px;top:424px}
.caption--3{left:26px;top:798px}
.caption--4{left:613px;top:798px}
.caption--5{left:26px;top:1163px}

.hero-photo{position:absolute;left:0;top:0;width:100%;height:calc(var(--panel-h) - var(--band-h))}
.hero-photo--cafe{background:linear-gradient(110deg,#3a3a38 0%,#6b5c3e 40%,#b98a32 70%,#8a6a3a 100%)}
.hero-photo--salad{background:radial-gradient(ellipse at 55% 45%,#9a5a3a 0%,#6b4a33 35%,#3e6b2a 70%,#2a4a1e 100%)}
.hero-photo--cups{background:linear-gradient(160deg,#6b5222 0%,#9a7a3a 35%,#bfb8a8 65%,#7a7670 100%)}
.hero-photo--cheese{background:radial-gradient(ellipse at 50% 55%,#f0d089 0%,#d9a652 45%,#a9752e 100%)}
.hero-photo--facade{background:linear-gradient(90deg,#2a2a26 0%,#3a3a30 40%,#7a3a28 60%,#6a3222 90%,#3a2a22 100%)}

.brand{position:absolute;left:56px;top:22px;color:var(--white);font-weight:700;font-size:20px;letter-spacing:1px}
.nav{position:absolute;left:210px;top:27px;display:flex;gap:11px;font-size:6.2px;font-weight:600;color:var(--white);text-transform:uppercase;letter-spacing:.3px}
.nav span::before{content:"";display:inline-block;width:6px;height:5px;border:0.8px solid var(--white);border-radius:1px;margin-right:2px;vertical-align:-1px}

.btn{position:absolute;left:50%;transform:translateX(-50%);width:70px;height:16px;background:var(--white);color:var(--brand-red);font-size:7.5px;font-weight:600;text-transform:uppercase;letter-spacing:.6px;text-align:center;line-height:17px;border-radius:2px}
.dots{position:absolute;top:240px;left:50%;transform:translateX(-50%);display:flex;gap:8.5px}
.dots i{width:6px;height:6px;border:1px solid var(--white);border-radius:50%}
.dots i.on{background:var(--white)}

.band{position:absolute;left:0;bottom:0;width:100%;height:var(--band-h);background:var(--brand-red)}
.social{position:absolute;left:66px;top:11px;display:flex;gap:11px}
.social i{width:16px;height:16px;border-radius:50%;background:var(--white)}
.footer-nav{position:absolute;left:210px;top:12px;font-size:5.8px;font-weight:600;color:var(--white);text-transform:uppercase;letter-spacing:.3px;word-spacing:1px}
.footer-copy{position:absolute;left:210px;top:22px;font-size:5px;color:var(--white);font-variant:small-caps;letter-spacing:.3px}

.headline{position:absolute;color:var(--white);font-variant:small-caps;text-transform:none;font-weight:600;white-space:nowrap}
.headline small{font-size:.55em}

/* slide 1 */
.s1-the{left:0;width:100%;top:108px;text-align:center;font-size:13px}
.s1-main{left:0;width:100%;top:124px;text-align:center;font-size:28px;letter-spacing:.5px}
.s1-sub{left:0;width:100%;top:153px;text-align:center;font-size:26px}

/* slide 2 */
.s2-quality{left:97px;top:126px;font-size:30px;font-weight:300;color:transparent;-webkit-text-stroke:1.3px var(--white);letter-spacing:3px;text-transform:uppercase;font-variant:normal}
.s2-food{left:164px;top:152px;font-size:30px;font-weight:300;color:transparent;-webkit-text-stroke:1.3px var(--white);letter-spacing:3px;text-transform:uppercase;font-variant:normal}
.s2-note{position:absolute;left:291px;top:125px;width:271px;height:53px;background:rgba(0,0,0,.12);border-left:1px solid rgba(255,255,255,.5);padding:5px 8px;color:var(--white);font-size:7.3px;line-height:9.6px;text-transform:uppercase;letter-spacing:.3px}

/* slide 3 */
.s3-l1{left:0;width:100%;top:101px;text-align:center;font-size:14px}
.s3-l2{left:0;width:100%;top:118px;text-align:center;font-size:28px}
.s3-l3{left:0;width:100%;top:146px;text-align:center;font-size:13px}
.s3-l3 .boxed{display:inline-block;border:1.5px solid var(--white);padding:1px 3px 0;font-size:27px;vertical-align:-2px;margin:0 2px}

/* slide 4 */
.s4-l1{left:93px;top:118px;font-size:28px}
.s4-l2{left:93px;top:147px;font-size:13px}
.s4-l2 .highlight{display:inline-block;background:var(--white);color:var(--gold);font-size:27px;padding:1px 4px 0;margin-left:3px;vertical-align:-4px}

/* slide 5 */
.hours{position:absolute;left:56px;top:91px;width:238px;height:114px;border:1.5px solid rgba(255,255,255,.85);background:rgba(255,255,255,.08);color:var(--white);text-align:center}
.hours h2{font-variant:small-caps;font-weight:600;font-size:17px;margin-top:10px;letter-spacing:.5px}
.hours p{font-size:8px;margin-top:10px;line-height:14px}
.hours p b{font-variant:small-caps;font-weight:600;font-size:10px}
.hours .reserve{margin-top:10px;font-variant:small-caps;font-size:10px;font-weight:600}
.wall-name{position:absolute;left:380px;top:118px;width:104px;text-align:center;color:var(--brand-red);font-weight:700;font-size:21px;letter-spacing:.5px}
.s5-btn{left:435px;top:176px}
</style>
</head>
<body>
<h1 class="board-title">HOME PAGE</h1>

<!-- Slide 1 -->
<section class="screen screen--1">
  <div class="hero-photo hero-photo--cafe" role="img" aria-label="Restaurant interior with counter, pendant lights and steel-framed windows"></div>
  <div class="brand">BRIMLOW</div>
  <nav class="nav"><span>Our Story</span><span>Menu</span><span>Reservations</span><span>Catering &amp; Delivery</span><span>Contact</span></nav>
  <div class="headline s1-the">The</div>
  <div class="headline s1-main">Mediterranean’s</div>
  <div class="headline s1-sub"><small>Finest</small> Produce</div>
  <div class="btn" style="top:211px">View Now</div>
  <div class="dots"><i class="on"></i><i></i><i></i><i></i><i></i></div>
  <footer class="band">
    <div class="social"><i></i><i></i><i></i><i></i></div>
    <div class="footer-nav">Home &nbsp;|&nbsp; Our Story &nbsp;|&nbsp; Menu &nbsp;|&nbsp; Reservations &nbsp;|&nbsp; Catering &amp; Delivery &nbsp;|&nbsp; Contact</div>
    <div class="footer-copy">© 2017 Brimlow</div>
  </footer>
</section>
<p class="caption caption--1">click to <b>Contact</b></p>

<!-- Slide 2 -->
<section class="screen screen--2">
  <div class="hero-photo hero-photo--salad" role="img" aria-label="Close-up of a fresh salad with greens, cured meat, shaved cheese and egg"></div>
  <div class="brand">BRIMLOW</div>
  <nav class="nav"><span>Our Story</span><span>Menu</span><span>Reservations</span><span>Catering &amp; Delivery</span><span>Contact</span></nav>
  <div class="headline s2-quality">Quality</div>
  <div class="headline s2-food">Food</div>
  <div class="s2-note">Is devotion to seasonal,<br>finest ingredients, and<br>meticulous care in<br>bringing it to life<br>on the plate.</div>
  <div class="btn" style="top:206px">View Now</div>
  <div class="dots"><i></i><i class="on"></i><i></i><i></i><i></i></div>
  <footer class="band">
    <div class="social"><i></i><i></i><i></i><i></i></div>
    <div class="footer-nav">Home &nbsp;|&nbsp; Our Story &nbsp;|&nbsp; Menu &nbsp;|&nbsp; Reservations &nbsp;|&nbsp; Catering &amp; Delivery &nbsp;|&nbsp; Contact</div>
    <div class="footer-copy">© 2017 Brimlow</div>
  </footer>
</section>
<p class="caption caption--2">click to <b>Contact</b></p>

<!-- Slide 3 -->
<section class="screen screen--3">
  <div class="hero-photo hero-photo--cups" role="img" aria-label="Coffee bar with rows of white cups under warm lights and a colourful mural"></div>
  <div class="brand">BRIMLOW</div>
  <nav class="nav"><span>Our Story</span><span>Menu</span><span>Reservations</span><span>Catering &amp; Delivery</span><span>Contact</span></nav>
  <div class="headline s3-l1">Tables will only be held</div>
  <div class="headline s3-l2"><small>for</small> 15 Minutes</div>
  <div class="headline s3-l3">Past the<span class="boxed">Reservation</span>time.</div>
  <div class="btn" style="top:206px">View Now</div>
  <div class="dots"><i></i><i></i><i class="on"></i><i></i><i></i></div>
  <footer class="band">
    <div class="social"><i></i><i></i><i></i><i></i></div>
    <div class="footer-nav">Home &nbsp;|&nbsp; Our Story &nbsp;|&nbsp; Menu &nbsp;|&nbsp; Reservations &nbsp;|&nbsp; Catering &amp; Delivery &nbsp;|&nbsp; Contact</div>
    <div class="footer-copy">© 2017 Brimlow</div>
  </footer>
</section>
<p class="caption caption--3">click to <b>Contact</b></p>

<!-- Slide 4 -->
<section class="screen screen--4">
  <div class="hero-photo hero-photo--cheese" role="img" aria-label="Close-up of golden grilled cheese slices"></div>
  <div class="brand">BRIMLOW</div>
  <nav class="nav"><span>Our Story</span><span>Menu</span><span>Reservations</span><span>Catering &amp; Delivery</span><span>Contact</span></nav>
  <div class="headline s4-l1"><small>a</small> Special Event</div>
  <div class="headline s4-l2">Requires a<span class="highlight">Unique Experience</span>.</div>
  <div class="btn" style="top:206px">View Now</div>
  <div class="dots"><i></i><i></i><i></i><i class="on"></i><i></i></div>
  <footer class="band">
    <div class="social"><i></i><i></i><i></i><i></i></div>
    <div class="footer-nav">Home &nbsp;|&nbsp; Our Story &nbsp;|&nbsp; Menu &nbsp;|&nbsp; Reservations &nbsp;|&nbsp; Catering &amp; Delivery &nbsp;|&nbsp; Contact</div>
    <div class="footer-copy">© 2017 Brimlow</div>
  </footer>
</section>
<p class="caption caption--4">click to <b>Contact</b></p>

<!-- Slide 5 -->
<section class="screen screen--5">
  <div class="hero-photo hero-photo--facade" role="img" aria-label="Restaurant entrance at night with brick wall, glazed window, plants and a wooden door"></div>
  <div class="brand">BRIMLOW</div>
  <nav class="nav"><span>Our Story</span><span>Menu</span><span>Reservations</span><span>Catering &amp; Delivery</span><span>Contact</span></nav>
  <div class="hours">
    <h2>Opening Hours</h2>
    <p>Daily from: <b>8am – 10pm</b><br>Friday: <b>Closed from Noon – 2pm</b></p>
    <div class="reserve">Make a reservation</div>
  </div>
  <div class="wall-name">BRIMLOW</div>
  <div class="btn s5-btn">Visit Us</div>
  <div class="dots"><i></i><i></i><i></i><i></i><i class="on"></i></div>
  <footer class="band">
    <div class="social"><i></i><i></i><i></i><i></i></div>
    <div class="footer-nav">Home &nbsp;|&nbsp; Our Story &nbsp;|&nbsp; Menu &nbsp;|&nbsp; Reservations &nbsp;|&nbsp; Catering &amp; Delivery &nbsp;|&nbsp; Contact</div>
    <div class="footer-copy">© 2017 Brimlow</div>
  </footer>
</section>
<p class="caption caption--5">click to <b>Contact</b></p>
</body>
</html>
```